1887 Basins & Spouts Business Card

I'm wanting to get a business card designed. Our business is 1887 Basins & Spouts
Details for the card:

1887 Basins & Spouts
Name: Warren Tobbit
Email: warren@1887basinsandspouts.com.au
Website: www.1887basinsandspouts.com.au
Mobile: 0438 169 204
Phone: 02 6187 4932

Font of Basins & Spouts is called Snell Roundhand. Not sue what font logo text is.

I'm thinking two sided but it doesn't have to be.

```html
<!DOCTYPE html>
<html lang="en">
<head>
<meta charset="utf-8">
<title>1887 Basins &amp; Spouts Business Card</title>
<link rel="stylesheet" href="https://fonts.googleapis.com/css2?family=Pinyon+Script&family=Open+Sans:wght@400&display=swap">
<style>
  :root {
    --backdrop: #2a2a2b;
    --card: #0d0d0d;
    --card-edge: #1a1a1a;
    --ink: #f4f4f4;
    --ink-soft: #a9a9a9;
    --rule: #6a6a6a;
    --icon-bg: #ededed;
    --icon-ink: #111111;
  }
  * { box-sizing: border-box; margin: 0; padding: 0; }
  html, body { width: 1200px; height: 900px; overflow: hidden; }
  body {
    background: var(--backdrop);
    position: relative;
    font-family: "Open Sans", Arial, sans-serif;
  }
  .card {
    position: absolute;
    width: 520px;
    height: 317px;
    background: linear-gradient(160deg, var(--card-edge), var(--card) 60%);
    box-shadow: 0 18px 40px rgba(0,0,0,0.55);
    overflow: hidden;
  }
  .card--front { left: 430px; top: 100px; }
  .card--back { left: 250px; top: 470px; }

  .brand {
    position: absolute;
    left: 50px;
    top: 112px;
    display: flex;
    align-items: center;
    gap: 16px;
  }
  .brand__mark {
    width: 70px;
    height: 70px;
    border: 2px solid var(--ink);
    border-radius: 50%;
    flex: none;
  }
  .brand__name {
    font-family: "Pinyon Script", cursive;
    font-size: 34px;
    color: var(--ink);
    white-space: nowrap;
  }
  .tagline {
    position: absolute;
    left: 136px;
    top: 184px;
    font-size: 11px;
    color: var(--ink-soft);
    letter-spacing: 0.2px;
    white-space: nowrap;
  }

  .person {
    position: absolute;
    left: 0;
    right: 0;
    top: 62px;
    text-align: center;
    font-family: "Pinyon Script", cursive;
    font-weight: 400;
    font-size: 40px;
    color: var(--ink);
  }
  .divider {
    position: absolute;
    left: 140px;
    right: 140px;
    top: 128px;
    display: flex;
    align-items: center;
    gap: 8px;
  }
  .divider::before, .divider::after {
    content: "";
    flex: 1;
    height: 1px;
    background: var(--rule);
  }
  .icon {
    width: 20px;
    height: 20px;
    display: block;
  }
  .contacts {
    position: absolute;
    left: 0;
    right: 0;
    top: 154px;
    text-align: center;
    list-style: none;
    font-size: 15px;
    line-height: 21px;
    color: var(--ink-soft);
  }
</style>
</head>
<body>
  <section class="card card--front" aria-label="Card front">
    <div class="brand">
      <span class="brand__mark"></span>
      <span class="brand__name">1887 Basins &amp; Spouts</span>
    </div>
    <p class="tagline">Pairing classic elegance with everyday dependable use</p>
  </section>

  <section class="card card--back" aria-label="Card back">
    <h1 class="person">Warren Tobbit</h1>
    <div class="divider">
      <svg class="icon" viewBox="0 0 20 20" aria-label="Phone"><rect width="20" height="20" rx="4" fill="var(--icon-bg)"/><path d="M6 5c1 0 1.5 2.5 1 3.2-.4.5-.4.9.2 1.8.8 1.2 1.6 2 2.5 2.3.6.2 1 0 1.4-.4.6-.5 3 .3 2.9 1.3-.2 1.6-2 2.2-3.6 1.6C7.7 13.9 5.2 10.8 4.6 8 4.3 6.5 4.9 5 6 5z" fill="var(--icon-ink)"/></svg>
      <svg class="icon" viewBox="0 0 20 20" aria-label="Mobile"><rect width="20" height="20" rx="4" fill="var(--icon-bg)"/><rect x="6.5" y="3.5" width="7" height="13" rx="1.2" fill="var(--icon-ink)"/><rect x="7.7" y="5" width="4.6" height="8.5" fill="var(--icon-bg)"/></svg>
      <svg class="icon" viewBox="0 0 20 20" aria-label="Email"><rect width="20" height="20" rx="4" fill="var(--icon-bg)"/><rect x="4" y="6" width="12" height="8.5" fill="var(--icon-ink)"/><path d="M4.5 6.5 10 11l5.5-4.5" stroke="var(--icon-bg)" stroke-width="1.2" fill="none"/></svg>
      <svg class="icon" viewBox="0 0 20 20" aria-label="Website"><rect width="20" height="20" rx="4" fill="var(--icon-bg)"/><circle cx="10" cy="10" r="5.5" fill="var(--icon-ink)"/><path d="M4.5 10h11M10 4.5c-2.4 3-2.4 8 0 11M10 4.5c2.4 3 2.4 8 0 11" stroke="var(--icon-bg)" stroke-width="0.9" fill="none"/></svg>
    </div>
    <ul class="contacts">
      <li>0438 169 204</li>
      <li>02 6187 4932</li>
      <li>warren@1887basinsandspouts.com.au</li>
      <li>www.1887basinsandspouts.com.au</li>
    </ul>
  </section>
</body>
</html>
```